Crafted Ember Website

Would like a website designed for my fitness and nutrition coaching company Craft Ember. I have a company logo and would like to keep the page layout clean and simple. Needs to look great on computer and mobile devices.

Target Market(s)

Target market is individuals looking to make changes in their health and nutrition with the help of an online coach.

Industry/Entity Type

Fitness

Number of Pages Required

2 page

Colors
3176b5
0355a3
85acd3
cedeed
f8fcfd
ffffff

Requirements
Must have
• The first page should have the company logo and name towards the top and below that client before and after photos scrolling or displaying in some manner. Also would like a section that states services offered and a section about myself since I am the primary coach for clients.

```html
<!DOCTYPE html>
<html lang="en">
<head>
<meta charset="utf-8">
<title>Crafted Ember — Fitness &amp; Nutrition Coaching</title>
<link rel="stylesheet" href="https://fonts.googleapis.com/css2?family=Roboto:ital,wght@0,300;0,400;0,500;0,700;1,300;1,700&display=swap">
<style>
:root{
  --blue:#3176b5;
  --blue-bright:#2a84e6;
  --blue-deep:#0355a3;
  --blue-soft:#85acd3;
  --blue-pale:#cedeed;
  --ice:#f8fcfd;
  --white:#ffffff;
  --ink:#1e2430;
  --text:#555b66;
  --muted:#8a9099;
  --footer:#222836;
  --footer-base:#1a1f2b;
}
*{margin:0;padding:0;box-sizing:border-box}
html,body{width:1200px;height:2242px;overflow:hidden}
body{font-family:'Roboto',Arial,sans-serif;color:var(--text);background:var(--white);position:relative}

/* header */
.site-header{position:absolute;left:0;top:0;width:1200px;height:62px;background:rgba(255,255,255,.88);z-index:5}
.brand{position:absolute;left:46px;top:12px;display:flex;align-items:center;gap:9px;font-size:11px;font-weight:500;color:var(--blue);letter-spacing:.4px;text-transform:uppercase}
.brand-mark{width:36px;height:36px;border:2px solid var(--blue);border-radius:4px}
.main-nav{position:absolute;left:0;top:25px;font-size:9px;font-weight:500;color:var(--ink);text-transform:uppercase;white-space:nowrap}
.main-nav span{position:absolute;top:0}
.main-nav .active{color:var(--blue)}
.main-nav .active:after{content:"";position:absolute;left:0;right:0;top:15px;height:2px;background:var(--blue)}
.hotline{position:absolute;left:864px;top:21px;font-size:9px;font-weight:700;color:var(--ink);white-space:nowrap}
.hotline b{font-size:15px;font-weight:500;color:var(--blue);margin-left:4px}
.header-social{position:absolute;left:1083px;top:27px;display:flex;gap:11px}
.header-social i{width:7px;height:7px;border-radius:50%;background:#7b8593;display:block}

/* hero */
.hero{position:absolute;left:0;top:0;width:1200px;height:530px;background:linear-gradient(100deg,#6f9a3c 0%,#9cbd52 30%,#b9c98a 55%,#d6b79a 70%,#6f8f45 100%)}
.hero h1{position:absolute;left:233px;top:155px;font-size:37px;line-height:47px;font-style:italic;font-weight:700;color:var(--white)}
.hero p{position:absolute;left:233px;top:272px;width:395px;font-size:10.5px;line-height:18.7px;color:var(--white)}
.btn{position:absolute;display:flex;align-items:center;justify-content:center;background:var(--blue-bright);color:var(--white);font-size:8px;font-weight:700;text-transform:uppercase;border-radius:16px;box-shadow:0 6px 14px rgba(42,132,230,.35)}
.hero .btn{left:233px;top:385px;width:145px;height:28px}
.slider-dots{position:absolute;left:582px;top:505px;display:flex;gap:7px}
.slider-dots i{width:7px;height:7px;border:1px solid var(--white);border-radius:50%;display:block}
.slider-dots .on{background:var(--white)}
.slider-arrow{position:absolute;left:108px;top:272px;width:12px;height:12px;border-left:1px solid rgba(255,255,255,.6);border-bottom:1px solid rgba(255,255,255,.6);transform:rotate(45deg)}

/* services */
.section-title{position:absolute;left:0;width:1200px;text-align:center;font-size:30px;font-weight:400;color:var(--ink)}
.section-title:after{content:"";position:absolute;left:578px;top:48px;width:44px;height:3px;background:var(--blue)}
.service-card{position:absolute;top:655px;width:231px;height:163px;overflow:hidden}
.service-card .label{position:absolute;left:15px;bottom:14px;font-size:11px;font-weight:500;color:var(--white)}
.card-nutrition{left:235px;background:linear-gradient(135deg,#7fae4a,#a5c65a 50%,#c98a3a)}
.card-workout{left:484px;background:linear-gradient(135deg,#56664a,#3d4a3a)}
.card-workout .overlay{position:absolute;left:0;top:0;right:0;bottom:0;background:rgba(20,25,20,.45);padding:24px 24px;color:var(--white)}
.card-workout h4{font-size:10px;font-weight:500;margin-bottom:7px}
.card-workout p{font-size:9.5px;line-height:16.4px;white-space:nowrap}
.card-workout .more{display:block;margin-top:7px;font-size:7px;text-decoration:underline}
.card-support{left:734px;background:linear-gradient(135deg,#9ec7e8,#f2d08a 45%,#6fae5c)}

.feature{position:absolute;width:330px}
.feature svg{position:absolute;left:0;top:0}
.feature h3{position:absolute;left:48px;top:0;font-size:11px;font-weight:500;color:var(--ink);white-space:nowrap}
.feature p{position:absolute;left:48px;top:18px;width:300px;font-size:9px;line-height:16.4px;color:var(--muted);white-space:nowrap}

/* stats */
.stats{position:absolute;left:0;top:1118px;width:1200px;height:172px;background:linear-gradient(180deg,#3a4a5a,#2d3d48)}
.stat{position:absolute;top:70px;display:flex;align-items:center;gap:12px;color:var(--white)}
.stat .num{font-size:32px;font-weight:300;letter-spacing:-1px}
.stat .cap{font-size:9px;font-weight:500;line-height:14px;text-transform:uppercase}

/* about */
.about h2{position:absolute;left:297px;top:1383px;font-size:30px;font-weight:400;color:var(--ink)}
.about .role{position:absolute;left:297px;top:1426px;font-size:9px;font-style:italic;color:#b5b9bf}
.about .lead{position:absolute;left:297px;top:1455px;font-size:9px;color:var(--ink)}
.about .body{position:absolute;left:297px;top:1486px;width:325px;font-size:10.5px;line-height:13.5px;color:var(--text)}
.about .btn{left:297px;top:1594px;width:101px;height:28px}
.coach-photo{position:absolute;left:672px;top:1356px;width:231px;height:280px;background:linear-gradient(180deg,#d9c7a8,#e8dcc6 60%,#cdb996);box-shadow:0 8px 20px rgba(0,0,0,.18)}

/* call to action */
.cta{position:absolute;left:0;top:1706px;width:1200px;height:300px;background:linear-gradient(100deg,#3c4656,#4c5462 55%,#6a5650 80%,#4d5060)}
.cta h2{position:absolute;left:233px;top:70px;font-size:35px;font-weight:400;color:var(--white)}
.cta p{position:absolute;left:233px;top:128px;font-size:11.5px;line-height:22px;color:var(--white);white-space:nowrap}
.cta .btn{left:233px;top:194px;width:111px;height:28px}

/* footer */
.site-footer{position:absolute;left:0;top:2006px;width:1200px;height:204px;background:var(--footer);color:#b9bec7}
.footer-brand{position:absolute;left:233px;top:38px;display:flex;align-items:center;gap:10px;font-size:11px;font-weight:500;color:var(--white);letter-spacing:.4px;text-transform:uppercase}
.footer-brand .brand-mark{border-color:var(--white);width:36px;height:36px}
.contact-list{position:absolute;left:233px;top:112px;font-size:8px;line-height:19px}
.contact-list div{display:flex;align-items:center;gap:12px}
.links-head{position:absolute;left:467px;top:107px;font-size:8px;font-weight:700;color:var(--white)}
.footer-link{position:absolute;font-size:8px}
.footer-social{position:absolute;left:820px;top:137px;display:flex;gap:8px}
.footer-social i{width:24px;height:24px;border-radius:50%;background:#343b4a;display:block}
.footer-social .hi{background:var(--blue-bright)}
.copyright{position:absolute;left:0;top:2210px;width:1200px;height:32px;background:var(--footer-base);text-align:center;font-size:8px;line-height:32px;color:#6c7280}
</style>
</head>
<body>

<section class="hero" role="img" aria-label="Photo of a smiling woman running outdoors with earphones against green foliage">
  <span class="slider-arrow"></span>
  <h1>Inspiring you to live<br>a healthier lifestyle.</h1>
  <p>Craft Ember look at exercise, eating, wellness and food not just as calories and weight loss, but also emotional, mental, physical, and spiritual terms. An Integrative with Crafted Ember who's providing services in area knows like state of mind, health history background, as well as sleep patterns.</p>
  <a class="btn">Learn more</a>
  <div class="slider-dots"><i></i><i class="on"></i><i></i></div>
</section>

<header class="site-header">
  <div class="brand"><span class="brand-mark"></span>Crafted Ember</div>
  <nav class="main-nav">
    <span class="active" style="left:472px">Home</span>
    <span style="left:527px">About</span>
    <span style="left:589px">Services</span>
    <span style="left:660px">Program &amp; Plan</span>
    <span style="left:762px">Contact</span>
  </nav>
  <div class="hotline">HOTLINE:<b>1 (800) 555-0142</b></div>
  <div class="header-social"><i></i><i></i><i></i><i></i></div>
</header>

<h2 class="section-title" style="top:574px">Services</h2>

<div class="service-card card-nutrition" role="img" aria-label="Photo of fresh vegetables and fruit">
  <span class="label">Nutrition Strategies</span>
</div>
<div class="service-card card-workout" role="img" aria-label="Photo of a group running outdoors">
  <div class="overlay">
    <h4>Workout Routines</h4>
    <p>Finding a workout is as easy as scrolling<br>down, picking out the session that<br>matches your goals, andgetting your<br>butt to the gym!</p>
    <span class="more">READ MORE</span>
  </div>
</div>
<div class="service-card card-support" role="img" aria-label="Photo of a group joining hands in a huddle">
  <span class="label">Support &amp; Motivation</span>
</div>

<div class="feature" style="left:233px;top:898px">
  <svg width="30" height="30" viewBox="0 0 30 30" fill="none" stroke="#3176b5" stroke-width="1.4"><rect x="2" y="13" width="26" height="10" rx="2"/><path d="M6 13v4M10 13v3M14 13v4M18 13v3M22 13v4"/><path d="M12 8c2-4 6-4 8 0"/></svg>
  <h3>Nutrition Strategies</h3>
  <p>Keep reading to learn about why Crafted Ember is the career<br>you've been looking for.</p>
</div>
<div class="feature" style="left:606px;top:900px">
  <svg width="30" height="30" viewBox="0 0 30 30" fill="none" stroke="#3176b5" stroke-width="1.4"><rect x="8" y="7" width="14" height="17" rx="3"/><path d="M11 7V3h8v4M11 24v4h8v-4"/><path d="M12 15l2 2 4-4"/></svg>
  <h3>Online Coaching</h3>
  <p>Keep reading to learn about why Crafted Ember is the career<br>you've been looking for.</p>
</div>
<div class="feature" style="left:233px;top:995px">
  <svg width="30" height="30" viewBox="0 0 30 30" fill="none" stroke="#3176b5" stroke-width="1.4"><rect x="6" y="4" width="18" height="24" rx="2"/><path d="M11 4V2h8v2"/><path d="M10 11h10M10 16h10M10 21h10"/></svg>
  <h3>Workout Routines</h3>
  <p>Keep reading to learn about why Crafted Ember is the career<br>you've been looking for.</p>
</div>
<div class="feature" style="left:606px;top:992px">
  <svg width="34" height="30" viewBox="0 0 34 30" fill="none" stroke="#3176b5" stroke-width="1.4"><path d="M17 26C5 17 2 12 4 7c2-5 9-5 13 1 4-6 11-6 13-1 2 5-1 10-13 19z"/><path d="M4 15h8l2-4 3 7 2-3h11"/></svg>
  <h3 style="left:52px">Support &amp; Motivation</h3>
  <p style="left:52px">Keep reading to learn about why Crafted Ember is the career<br>you've been looking for.</p>
</div>

<section class="stats" role="img" aria-label="Background photo of a woman stretching in a forested valley">
  <div class="stat" style="left:233px"><span class="num">10</span><span class="cap">Years of<br>Experience</span></div>
  <div class="stat" style="left:438px"><span class="num">190</span><span class="cap">Workout<br>Sessions</span></div>
  <div class="stat" style="left:642px"><span class="num">150</span><span class="cap">Happy<br>Customers</span></div>
  <div class="stat" style="left:864px"><span class="num">90</span><span class="cap">Days of<br>Program</span></div>
</section>

<section class="about">
  <h2>Hi, I'm Sam Rivera</h2>
  <div class="role">Owner/Founder, Executive Coach</div>
  <div class="lead">Inspiring you to live a healthier lifestyle.</div>
  <p class="body">Maecenas iaculis ex id metus ullamcorper rhoncus. Vestibulum ultrices sed arcu ut feugiat. Maecenas aliquet sollicitudin nisl in malesuada. Donec felis ligula, vulputate lobortis hendrerit ac, commodo quis ante. Donec molestie leo eu urna molestie, eu hendrerit risus venenatis. Suspendisse potenti.</p>
  <a class="btn">About us</a>
  <div class="coach-photo" role="img" aria-label="Photo of the coach doing a push-up on the beach"></div>
</section>

<section class="cta" role="img" aria-label="Background photo of a smiling woman in a kitchen holding an apple">
  <h2>3 months with a Health Coach</h2>
  <p>Start working on your body today, and with the individual fitness program, already in 90 days you<br>will see a totally different girl in the mirror!</p>
  <a class="btn">Contact us</a>
</section>

<footer class="site-footer">
  <div class="footer-brand"><span class="brand-mark"></span>Crafted Ember</div>
  <div class="contact-list">
    <div><svg width="8" height="8" viewBox="0 0 10 10" fill="#b9bec7"><path d="M2 0l2 2-1 2c1 1 2 2 3 3l2-1 2 2-2 2C4 10 0 6 0 2z"/></svg>+1 800 555 0142</div>
    <div><svg width="8" height="8" viewBox="0 0 10 8" fill="#b9bec7"><path d="M0 0h10v8H0z"/></svg>info@craftedember.com</div>
    <div><svg width="8" height="8" viewBox="0 0 8 10" fill="#b9bec7"><path d="M4 0a4 4 0 0 1 4 4c0 3-4 6-4 6S0 7 0 4a4 4 0 0 1 4-4z"/></svg>12 Address</div>
  </div>
  <div class="links-head">LINKS</div>
  <span class="footer-link" style="left:467px;top:140px">Home</span>
  <span class="footer-link" style="left:467px;top:163px">About Us</span>
  <span class="footer-link" style="left:571px;top:140px">Services</span>
  <span class="footer-link" style="left:571px;top:163px">Programs and Plans</span>
  <span class="footer-link" style="left:696px;top:140px">Contac Us</span>
  <div class="footer-social"><i></i><i class="hi"></i><i></i><i></i></div>
</footer>
<div class="copyright">© 2017 Craft Ember. All rights reserved.</div>

</body>
</html>
```